Consulting Company needs business card design

We need a business card design for a new consulting and business solutions company based in Bermuda called Corvale Partners Limited. Looking for a double sided business card with one side only including the company logo thats attached and the other including contact information. Logo contains blue and turquoise colors and is fine to be on both sides of the card.
Contact Information for Business Card
Corvale Partners Limited
P.O. Box HM318
Devonshire DV BX
Bermuda
Name: Marcus Pellegrin
Position: Director
Telephone: 1 441 733 4906
Email: mpellegrin@corvale.example
Website: www.corvale.example

```html
<!DOCTYPE html>
<html lang="en">
<head>
<meta charset="utf-8">
<title>Corvale Partners Limited – Business Card</title>
<link rel="stylesheet" href="https://fonts.googleapis.com/css2?family=Roboto:wght@400;500;700&display=swap">
<style>
  :root {
    --stage: #d4d4d4;
    --card-white: #ffffff;
    --brand-blue: #29a3dd;
    --brand-teal: #0fb0b9;
    --front-start: #25a3e1;
    --front-end: #06b0b6;
    --ribbon-light: #d6eefa;
    --ribbon-mid: #7dcbe9;
    --text-grey: #444b50;
    --white: #ffffff;
  }
  * { margin: 0; padding: 0; box-sizing: border-box; }
  html, body {
    width: 1200px;
    height: 1000px;
    overflow: hidden;
    background: var(--stage);
    font-family: "Roboto", Arial, sans-serif;
  }
  .canvas { position: relative; width: 1200px; height: 1000px; }

  .card { position: absolute; width: 715px; height: 429px; overflow: hidden; }

  /* Front side */
  .card-front {
    left: 252px; top: 33px;
    background: linear-gradient(135deg, var(--front-start) 0%, var(--front-end) 100%);
  }
  .front-brand {
    position: absolute; left: 100px; top: 148px;
    display: flex; align-items: center; gap: 26px;
    color: var(--white); font-weight: 500;
  }
  .front-brand .brand-dot {
    width: 130px; height: 130px; border-radius: 50%; background: var(--white);
  }
  .front-brand .brand-name { line-height: 1; }
  .front-brand .brand-name-main { display: block; font-size: 78px; letter-spacing: 2px; }
  .front-brand .brand-name-sub { display: block; font-size: 27px; letter-spacing: 4.5px; margin-top: 10px; }

  /* Back side */
  .card-back { left: 248px; top: 538px; background: var(--card-white); }

  .ribbon-decor {
    position: absolute; left: 58px; top: 45px; width: 600px; height: 335px;
    border-radius: 50%;
    background: radial-gradient(ellipse at 55% 50%, var(--ribbon-mid) 0%, var(--ribbon-light) 45%, rgba(214,238,250,0) 72%);
    opacity: 0.55;
  }

  .back-brand {
    position: absolute; left: 48px; top: 138px;
    display: flex; align-items: center; gap: 12px;
    color: var(--brand-blue); font-weight: 500;
  }
  .back-brand .brand-dot { width: 44px; height: 44px; border-radius: 50%; background: var(--brand-blue); }
  .back-brand .brand-name { line-height: 1; }
  .back-brand .brand-name-main { display: block; font-size: 31px; letter-spacing: 1px; }
  .back-brand .brand-name-sub { display: block; font-size: 13px; letter-spacing: 2.2px; margin-top: 3px; }

  .postal-address {
    position: absolute; left: 128px; top: 216px;
    font-style: normal; color: var(--brand-teal);
    font-size: 19px; line-height: 25.5px;
  }

  .contact-person { position: absolute; left: 416px; top: 144px; }
  .person-name { color: var(--brand-blue); font-size: 30px; font-weight: 700; line-height: 1.1; }
  .person-title { color: var(--brand-blue); font-size: 20px; letter-spacing: 1.5px; margin-top: 1px; }

  .contact-list {
    position: absolute; left: 414px; top: 214px; list-style: none;
    color: var(--text-grey); font-size: 19.5px;
  }
  .contact-list li { display: flex; align-items: center; gap: 8px; height: 32px; }
  .contact-icon { width: 21px; height: 21px; flex: none; color: var(--brand-teal); }
  .contact-icon.at { font-size: 23px; font-weight: 700; line-height: 21px; text-align: center; }
  .web-highlight { color: var(--brand-blue); }
</style>
</head>
<body>
<main class="canvas">

  <section class="card card-front" aria-label="Business card front">
    <div class="front-brand">
      <span class="brand-dot" aria-hidden="true"></span>
      <span class="brand-name">
        <span class="brand-name-main">CORVALE</span>
        <span class="brand-name-sub">PARTNERS LIMITED</span>
      </span>
    </div>
  </section>

  <section class="card card-back" aria-label="Business card back">
    <div class="ribbon-decor" role="img" aria-label="Decorative flowing blue and turquoise ribbon swoosh"></div>

    <div class="back-brand">
      <span class="brand-dot" aria-hidden="true"></span>
      <span class="brand-name">
        <span class="brand-name-main">CORVALE</span>
        <span class="brand-name-sub">PARTNERS LIMITED</span>
      </span>
    </div>

    <address class="postal-address">
      P.O. Box HM318<br>
      Devonshire DV BX<br>
      Bermuda
    </address>

    <div class="contact-person">
      <p class="person-name">Marcus Pellegrin</p>
      <p class="person-title">Director</p>
    </div>

    <ul class="contact-list">
      <li>
        <svg class="contact-icon" viewBox="0 0 24 24" aria-hidden="true">
          <path fill="currentColor" d="M6.6 10.8c1.4 2.8 3.8 5.1 6.6 6.6l2.2-2.2c.3-.3.7-.4 1-.2 1.1.4 2.3.6 3.6.6.6 0 1 .4 1 1V20c0 .6-.4 1-1 1C10.6 21 3 13.4 3 4c0-.6.4-1 1-1h3.5c.6 0 1 .4 1 1 0 1.3.2 2.5.6 3.6.1.3 0 .7-.2 1L6.6 10.8z"/>
        </svg>
        <span>1 441 733 4906</span>
      </li>
      <li>
        <span class="contact-icon at" aria-hidden="true">@</span>
        <span>mpellegrin@corvale.example</span>
      </li>
      <li>
        <svg class="contact-icon" viewBox="0 0 24 24" aria-hidden="true" fill="none" stroke="currentColor" stroke-width="1.8">
          <circle cx="12" cy="12" r="9"/>
          <ellipse cx="12" cy="12" rx="4" ry="9"/>
          <path d="M3 12h18M4.5 7.5h15M4.5 16.5h15"/>
        </svg>
        <span>www.<span class="web-highlight">corvale</span>.example</span>
      </li>
    </ul>
  </section>

</main>
</body>
</html>
```